Email signature

I have an email signature, card and letter head and I would like the colours darker and more distinctive and I would like the contact details to be bigger and or easier to read as they are hard to read at the moment. The arrow watermark is fine I think.

Logo Text

VANTORA GUARD PTY LTD

Requirements
Nice to have
• The yellow type colour with the grey is good and I would like to retain that, but it looks washed out and too light on the screen. I like the arrows and I like the watermark arrows as well and I would like to retain the basic design.

```html
<!DOCTYPE html>
<html lang="en">
<head>
<meta charset="utf-8">
<title>Vantora Guard – Stationery Set</title>
<link rel="stylesheet" href="https://fonts.googleapis.com/css2?family=Didact+Gothic&family=Quicksand:wght@500;600;700&display=swap">
<style>
  :root {
    --yellow: #f2c200;
    --yellow-soft: #f7dc66;
    --charcoal: #2e2e2e;
    --grey: #444444;
    --ink: #111111;
    --paper: #ffffff;
    --edge: #ececec;
  }
  * { margin: 0; padding: 0; box-sizing: border-box; }
  html, body { width: 1200px; height: 848px; overflow: hidden; background: var(--paper); }
  .canvas { position: relative; width: 1200px; height: 848px; background: var(--paper); }

  .brand-name {
    position: absolute; text-align: center;
    font-family: "Quicksand", sans-serif; font-weight: 700; color: var(--charcoal);
    line-height: 1;
  }
  .brand-name span { display: block; }
  .brand-mark { position: absolute; background: var(--yellow); }

  .brand-main { left: 20px; top: 90px; width: 664px; }
  .brand-main .name { font-size: 56px; letter-spacing: 1px; }
  .brand-main .suffix { font-size: 24px; margin-top: 22px; letter-spacing: 1px; font-weight: 600; }
  .mark-main { left: 40px; top: 96px; width: 44px; height: 44px; }

  .card {
    position: absolute; background: var(--paper);
    box-shadow: 0 0 4px var(--edge), 0 0 1px var(--edge);
  }

  .card-front { left: 71px; top: 311px; width: 283px; height: 463px; }
  .card-front .tagline {
    position: absolute; left: 50%; top: 50%;
    transform: translate(-50%, -50%) rotate(-90deg);
    font-family: "Didact Gothic", sans-serif; font-size: 50px; color: var(--ink);
    letter-spacing: 1px; white-space: nowrap;
  }
  .arrow-placeholder {
    position: absolute; left: 71px; width: 141px; height: 102px;
    background: linear-gradient(180deg, #d9d9d9, var(--yellow-soft));
  }
  .arrow-top { top: 25px; }
  .arrow-bottom { top: 336px; background: linear-gradient(0deg, #d9d9d9, var(--yellow-soft)); }

  .card-back { left: 402px; top: 311px; width: 283px; height: 463px; }
  .card-back .person {
    position: absolute; left: 22px; top: 22px;
    font-family: "Didact Gothic", sans-serif; font-weight: 400; font-size: 42px; line-height: 1.08;
    color: var(--grey); letter-spacing: 1px;
  }
  .person .first { color: var(--yellow); }
  .contact-list { position: absolute; left: 12px; top: 170px; list-style: none; }
  .contact-list li {
    display: flex; align-items: center; height: 34px; margin-bottom: 33px;
    font-family: "Quicksand", sans-serif; font-weight: 700; font-size: 17px; color: var(--ink);
  }
  .contact-list svg { width: 28px; height: 28px; margin-right: 14px; flex: none; }
  .card-back .brand-name { left: 10px; top: 400px; width: 283px; }
  .card-back .brand-mark { left: 54px; top: 400px; width: 22px; height: 22px; }
  .brand-card .name { font-size: 15px; }
  .brand-card .suffix { font-size: 7px; margin-top: 4px; }

  .letterhead { left: 731px; top: 200px; width: 396px; height: 593px; }
  .letterhead .brand-name { left: 10px; top: 30px; width: 396px; }
  .letterhead .brand-mark { left: 62px; top: 30px; width: 26px; height: 26px; }
  .brand-letter .name { font-size: 18px; }
  .brand-letter .suffix { font-size: 7px; margin-top: 5px; }
  .address {
    position: absolute; left: 266px; top: 128px; font-style: normal;
    font-family: "Quicksand", sans-serif; font-weight: 700; font-size: 11px; line-height: 1.2; color: var(--ink);
  }
  .salutation {
    position: absolute; left: 64px; top: 192px;
    font-family: "Didact Gothic", sans-serif; font-size: 12px; color: #222;
  }
  .letter-body {
    position: absolute; left: 67px; top: 218px; width: 303px;
    font-family: "Didact Gothic", sans-serif; font-size: 9px; line-height: 12.4px; color: #222;
  }
  .letter-body p + p { margin-top: 22px; }
</style>
</head>
<body>
<main class="canvas">

  <span class="brand-mark mark-main" aria-hidden="true"></span>
  <div class="brand-name brand-main">
    <span class="name">VANTORA GUARD</span>
    <span class="suffix">PTY LTD</span>
  </div>

  <section class="card card-front">
    <div class="arrow-placeholder arrow-top" role="img" aria-label="Upward arrow watermark in charcoal and yellow"></div>
    <p class="tagline">security.</p>
    <div class="arrow-placeholder arrow-bottom" role="img" aria-label="Downward arrow watermark in charcoal and yellow"></div>
  </section>

  <section class="card card-back">
    <h1 class="person"><span class="first">LENA</span>MARSH<br>DIRECTOR</h1>
    <ul class="contact-list">
      <li>
        <svg viewBox="0 0 28 28" aria-hidden="true" fill="none" stroke="var(--yellow)" stroke-width="1.8">
          <rect x="7" y="2" width="14" height="24" rx="2"/>
          <line x1="7" y1="6" x2="21" y2="6"/>
          <line x1="7" y1="21" x2="21" y2="21"/>
          <circle cx="14" cy="23.5" r="0.8" fill="var(--yellow)"/>
        </svg>
        0400 555 219
      </li>
      <li>
        <svg viewBox="0 0 28 28" aria-hidden="true" fill="none" stroke="var(--yellow)" stroke-width="1.8" stroke-linejoin="round">
          <path d="M26 3 L2 12 L11 15 Z"/>
          <path d="M26 3 L11 15 L13 25 Z"/>
          <path d="M11 15 L16 19"/>
        </svg>
        lena@vantoraguard.net.au
      </li>
      <li>
        <svg viewBox="0 0 28 28" aria-hidden="true" fill="none" stroke="var(--yellow)" stroke-width="1.8">
          <circle cx="14" cy="14" r="11"/>
          <ellipse cx="14" cy="14" rx="5" ry="11"/>
          <line x1="3" y1="14" x2="25" y2="14"/>
          <path d="M5 8 H23 M5 20 H23"/>
        </svg>
        www.vantoraguard.net.au
      </li>
    </ul>
    <span class="brand-mark" aria-hidden="true"></span>
    <div class="brand-name brand-card">
      <span class="name">VANTORA GUARD</span>
      <span class="suffix">PTY LTD</span>
    </div>
  </section>

  <section class="card letterhead">
    <span class="brand-mark" aria-hidden="true"></span>
    <div class="brand-name brand-letter">
      <span class="name">VANTORA GUARD</span>
      <span class="suffix">PTY LTD</span>
    </div>
    <address class="address">adress<br>line 1<br>line 3<br>postcode</address>
    <p class="salutation">dear sir/madam</p>
    <div class="letter-body">
      <p>Thank you for your recent enquiry about our site security services. We are pleased to outline the patrol, alarm response and guarding options that suit your premises. Each plan includes trained staff, regular reporting and a named contact for every shift. Our team can visit your site this month to review access points, lighting and camera coverage, and to prepare a tailored proposal with clear costs. We look forward to working with you and to keeping your people and property safe around the clock.</p>
      <p>Please find attached our service schedule and insurance details for your records. Should you have any questions about rosters, response times or pricing, our office is open weekdays and our control room operates every hour of the year. We value clear communication and will keep you informed at each stage of the handover. Thank you again for considering our company.</p>
    </div>
  </section>

</main>
</body>
</html>
```